Web design for sitter site

We will be launching a sitter site in the coming months that focuses on sitters for children. The name of this site will be KidHaven.com
We will need:
1. main page design
2. site logo designed
3. subpages as well for the look of people's profiles, and job listings, etc (see links below)
We only need the design, photos, font files, etc. We do not need this site coded (no html), a ps job is fine.
Some competing sites in the space include - tendlyhub.com and vurl.com
http://www.brisk-minder.example/images/profile1.jpg
http://quenthollibrary.example/wp-content/uploads/2013/09/vurl-review.png
http://www.palvermont.example/hr/photos/tendly_hub2.jpg
Target Market(s)
Mothers of children, mainly women
Industry/Entity Type
Online
Look and feel

```html
<!DOCTYPE html>
<html lang="en">
<head>
<meta charset="utf-8">
<title>KidHaven – Choose Your Sitter</title>
<link href="https://fonts.googleapis.com/css2?family=Roboto+Condensed:ital,wght@0,300;0,400;0,700;1,400&display=swap" rel="stylesheet">
<style>
:root{
  --orange:#f47349;
  --header:#454545;
  --nav:rgba(170,170,170,.85);
  --dark:#2a2a2a;
  --page:#fdfbfb;
  --ink:#1e1e1e;
  --footer:#2f3b3d;
  --line:#cfcfcf;
  --white:#ffffff;
}
*{margin:0;padding:0;box-sizing:border-box}
html,body{width:1200px;height:2557px;overflow:hidden}
body{position:relative;background:var(--page);font-family:"Roboto Condensed",Arial,sans-serif;color:var(--ink)}
.abs{position:absolute}

/* header */
.hero-photo{left:0;top:0;width:1200px;height:762px;background:linear-gradient(160deg,#e9e4df 0%,#c9a58b 35%,#e7d3c2 55%,#d7b79a 75%,#f1ece8 100%)}
.topbar{left:0;top:0;width:1200px;height:124px;background:var(--header)}
.brand{left:150px;top:48px;display:flex;align-items:center;gap:14px;color:var(--white);font-size:42px;font-weight:400;letter-spacing:1px}
.brand .dot{width:26px;height:26px;border-radius:50%;background:var(--orange)}
.account{left:910px;top:0;height:29px;display:flex;background:var(--orange)}
.account a{color:var(--white);text-decoration:none;font-size:12px;line-height:29px;padding:0 7px}
.account a+a{border-left:1px solid rgba(255,255,255,.6)}
.callus{left:762px;top:42px;color:var(--white);font-size:24px;font-weight:400}

.mainnav{left:0;top:124px;width:1200px;height:58px;background:var(--nav)}
.mainnav a{position:absolute;top:0;height:58px;line-height:58px;color:var(--white);text-decoration:none;font-size:12px}
.mainnav a.active{background:var(--orange);padding:0 16px}

.search-band{left:0;top:603px;width:1200px;height:159px;background:rgba(255,255,255,.45)}
.search-title{left:264px;top:622px;font-size:34px;font-weight:300;color:#333;white-space:nowrap}
.search-title span{color:var(--orange);font-weight:400;margin-left:10px}
.search-input{left:264px;top:682px;width:558px;height:59px;background:rgba(255,255,255,.9);color:#cfcfcf;font-size:25px;font-weight:300;line-height:59px;padding-left:14px}
.search-btn{left:822px;top:682px;width:107px;height:59px;background:var(--dark);color:var(--white);font-size:26px;font-weight:300;text-align:center;line-height:59px}

/* welcome */
.welcome{left:0;top:762px;width:1200px;height:291px;background:var(--dark);color:var(--white);text-align:center}
.welcome h1{margin-top:20px;font-size:44px;font-weight:300}
.welcome h2{margin-top:8px;font-size:19px;font-weight:300;color:var(--orange)}
.welcome p{width:845px;margin:12px auto 0;font-size:12.5px;line-height:24px;color:#e6e6e6}

.section-title{left:0;width:1200px;text-align:center;font-size:40px;font-weight:300;color:var(--ink)}

/* cards */
.card{top:1178px;width:262px;height:378px;background:var(--dark);color:var(--white)}
.card .photo{height:157px}
.card h3{height:35px;line-height:35px;background:var(--orange);text-align:center;font-size:21px;font-weight:300}
.card p{padding:14px 14px 0;font-size:11px;line-height:20px;text-align:center;color:#e4e4e4;height:144px}
.card .cta{display:flex;align-items:center;justify-content:center;gap:12px;font-style:italic;font-size:17px}
.card .cta::before,.card .cta::after{content:"";width:54px;height:1px;background:var(--orange)}

.divider{left:150px;top:1604px;width:900px;height:2px;background:#e0dede}

/* steps */
.vline{left:586px;top:1739px;width:2px;height:341px;background:var(--line)}
.hline{left:250px;top:1892px;width:738px;height:2px;background:var(--line)}
.step{width:300px}
.step svg{position:absolute;left:-45px;top:-4px}
.step h4{font-size:23px;font-weight:400;color:var(--orange)}
.step p{margin-top:10px;font-size:12px;line-height:23px;color:var(--ink)}

/* testimonial */
.testimonial{left:0;top:2129px;width:1200px;height:285px;background:var(--orange);color:var(--white)}
.testimonial h2{position:absolute;left:0;top:22px;width:1200px;text-align:center;font-size:30px;font-weight:300}
.avatar{left:544px;top:2203px;width:88px;height:88px;border-radius:50%;background:#1e1e1e;padding:6px}
.avatar div{width:100%;height:100%;border-radius:50%;background:linear-gradient(#e8e2dc,#c9b8a9)}
.quote-mark{font-size:60px;font-family:Georgia,serif;font-weight:700;color:var(--white);line-height:1}
.quote-text{left:254px;top:2319px;width:680px;font-size:11px;line-height:20px;font-style:italic;color:var(--white)}
.quote-name{left:0;top:2369px;width:1200px;text-align:center;font-size:13px;font-weight:700;font-style:italic;color:#5a2d1e}

/* footer */
.footer{left:0;top:2414px;width:1200px;height:143px;background:var(--footer)}
.footnav a{position:absolute;top:2414px;height:61px;line-height:61px;font-size:11.5px;color:var(--white);text-decoration:none}
.footnav a.active{background:#e4e4e4;color:var(--ink);padding:0 16px}
.follow{left:907px;top:2476px;font-size:11px;color:#d6d6d6}
.social{left:907px;top:2502px;display:flex;gap:4px}
.social span{width:28px;height:28px;border-radius:3px}
.privacy{left:0;top:2516px;width:1200px;text-align:center;font-size:11px;color:#d6d6d6}
</style>
</head>
<body>

<div class="abs hero-photo" role="img" aria-label="Photo of a smiling mother lying in bed hugging her young daughter and son"></div>

<header class="abs topbar"></header>
<div class="abs brand"><span class="dot"></span>KIDHAVEN</div>
<nav class="abs account"><a href="#">LOG IN</a><a href="#">JOIN NOW</a></nav>
<div class="abs callus">CALL US ON -1300-482-617</div>

<nav class="abs mainnav">
  <a class="active" href="#" style="left:157px">WHAT WE CARE</a>
  <a href="#" style="left:300px">CHILD CARE</a>
  <a href="#" style="left:412px">ELDER CARE</a>
  <a href="#" style="left:520px">PET CARE</a>
  <a href="#" style="left:622px">HOW IT WORKS</a>
</nav>

<div class="abs search-band"></div>
<div class="abs search-title">LETS GET STARTED<span>CHOOSE YOUR SITTER</span></div>
<div class="abs search-input">SEARCH FOR CARE IN YOUR AREA</div>
<div class="abs search-btn">SEARCH</div>

<section class="abs welcome">
  <h1>WELCOME TO KIDHAVEN</h1>
  <h2>SED UT PERSPICIATIS UNDE OMNIS</h2>
  <p>Sed ut perspiciatis unde omnis iste natus error sit voluptatem accusantium doloremque laudantium, totam rem aperiam, eaque ipsa quae ab illo inventore veritatis et quasi architecto beatae vitae dicta sunt explicabo. Nemo enim ipsam voluptatem quia voluptas sit aspernatur aut odit aut fugit, sed quia consequuntur magni dolores eos qui ratione voluptatem sequi nesciunt. Neque porro quisquam est, qui dolorem ipsum quia dolor sit amet, consectetur, adipisci velit, sed quia non numquam eius modi tempora incidunt ut labore et dolore magnam aliquam quaerat voluptatem. Ut enim ad minima veniam, quis nostrum exercitationem ullam corporis suscipit laboriosam, nisi ut aliquid ex ea commodi consequatur?</p>
</section>

<h2 class="abs section-title" style="top:1093px">WHAT WE ARE</h2>

<article class="abs card" style="left:174px">
  <div class="photo" role="img" aria-label="Photo of a mother cuddling two children" style="background:linear-gradient(135deg,#f3efe9,#d8b59b 60%,#efe6dc)"></div>
  <h3>CHILD CARE</h3>
  <p>Sed ut perspiciatis unde omnis iste natus error sit voluptatem accusantium doloremque laudantium, totam rem aperiam, eaque ipsa quae ab illo inventore veritatis et quasi architecto beatae vitae dicta sunt explicabo.</p>
  <div class="cta">GET STARTED</div>
</article>
<article class="abs card" style="left:469px">
  <div class="photo" role="img" aria-label="Photo of a ginger cat held by its owner" style="background:linear-gradient(135deg,#f2eee8,#d49a62 55%,#e9ddd0)"></div>
  <h3>PET CARE</h3>
  <p>Sed ut perspiciatis unde omnis iste natus error sit voluptatem accusantium doloremque laudantium, totam rem aperiam, eaque ipsa quae ab illo inventore veritatis et quasi architecto beatae vitae dicta sunt explicabo.</p>
  <div class="cta">GET STARTED</div>
</article>
<article class="abs card" style="left:762px">
  <div class="photo" role="img" aria-label="Photo of cheerful elderly people giving thumbs up" style="background:linear-gradient(135deg,#d9c9bd,#c39a80 50%,#e3d6ca)"></div>
  <h3>ELDER CARE</h3>
  <p>Sed ut perspiciatis unde omnis iste natus error sit voluptatem accusantium doloremque laudantium, totam rem aperiam, eaque ipsa quae ab illo inventore veritatis et quasi architecto beatae vitae dicta sunt explicabo.</p>
  <div class="cta">GET STARTED</div>
</article>

<div class="abs divider"></div>

<h2 class="abs section-title" style="top:1638px">HOW IT WORKS</h2>

<div class="abs vline"></div>
<div class="abs hline"></div>

<div class="abs step" style="left:280px;top:1768px">
  <svg width="34" height="34" viewBox="0 0 34 34" aria-hidden="true"><path d="M3 9h28v20H3z" fill="#1e1e1e"/><path d="M6 9l18-6 3 6z" fill="#1e1e1e"/><circle cx="17" cy="17" r="4" fill="#fff"/><path d="M10 27c1-5 13-5 14 0z" fill="#fff"/></svg>
  <h4>SED UT PERSPICIATIS</h4>
  <p>Sed ut perspiciatis unde omnis iste natus error sit<br>voluptatem accusantium doloremque laudantium</p>
</div>
<div class="abs step" style="left:721px;top:1768px">
  <svg width="34" height="34" viewBox="0 0 34 34" aria-hidden="true"><circle cx="17" cy="12" r="9" fill="#1e1e1e"/><path d="M2 33c1-11 29-11 30 0z" fill="#1e1e1e"/></svg>
  <h4>SED UT PERSPICIATIS</h4>
  <p>Sed ut perspiciatis unde omnis iste natus error sit<br>voluptatem accusantium doloremque laudantium</p>
</div>
<div class="abs step" style="left:280px;top:1937px">
  <svg width="34" height="34" viewBox="0 0 34 34" aria-hidden="true"><path d="M17 31C6 22 1 17 1 10a8 8 0 0 1 16-2 8 8 0 0 1 16 2c0 7-5 12-16 21z" fill="#1e1e1e"/></svg>
  <h4>SED UT PERSPICIATIS</h4>
  <p>Sed ut perspiciatis unde omnis iste natus error sit<br>voluptatem accusantium doloremque laudantium</p>
</div>
<div class="abs step" style="left:721px;top:1937px">
  <svg width="34" height="34" viewBox="0 0 34 34" aria-hidden="true"><path d="M17 3l4.2 9 9.8 1.1-7.3 6.6 2 9.7L17 24.5l-8.7 4.9 2-9.7L3 13.1l9.8-1.1z" fill="none" stroke="#1e1e1e" stroke-width="3" stroke-linejoin="round"/></svg>
  <h4>SED UT PERSPICIATIS</h4>
  <p>Sed ut perspiciatis unde omnis iste natus error sit<br>voluptatem accusantium doloremque laudantium</p>
</div>

<section class="abs testimonial"><h2>TESTIMONIAL</h2></section>
<div class="abs avatar"><div role="img" aria-label="Portrait photo of the customer giving the testimonial"></div></div>
<div class="abs quote-mark" style="left:216px;top:2300px">&ldquo;</div>
<p class="abs quote-text">Lorem ipsum dolor sit amet, consectetur adipisicing elit, sed do eiusmod tempor incididunt ut labore et dolore magna aliqua. Ut enim ad minim veniam, quis nostrud exercitation ullamco laboris nisi ut aliquip ex ea commodo consequat.</p>
<div class="abs quote-mark" style="left:930px;top:2340px">&rdquo;</div>
<div class="abs quote-name">Toby</div>

<footer class="abs footer"></footer>
<nav class="footnav">
  <a class="active" href="#" style="left:268px">WHAT WE CARE</a>
  <a href="#" style="left:412px">CHILD CARE</a>
  <a href="#" style="left:525px">ELDER CARE</a>
  <a href="#" style="left:632px">PET CARE</a>
  <a href="#" style="left:735px">HOW IT WORKS</a>
</nav>
<div class="abs follow">Follow Us:</div>
<div class="abs social" aria-label="Social links">
  <span style="background:#3b5b98"></span>
  <span style="background:#3aa8dd"></span>
  <span style="background:#1c7bb5"></span>
  <span style="background:#555"></span>
</div>
<div class="abs privacy">Privacy / Copyright</div>

</body>
</html>
```